Forestry Mulching Business Cards

Business is called Ridgeline Clearing, We do forestry mulching which helps with wildfire mitigation, it helps reclaim your land. Just some ideas on what to say, get creative. I would like a Tramwell tracked skidsteer with a mulching head on it included somewhere, like the one i have attached in the photo. I would also like to add a groundhog popping out of the ground as a logo since i do not have one yet. Name and phone number and location should have a text slot, maybe include what brush removal/control does for you on the back in bulletins. I know i didnt make this very detailed but i want you guys to get creative!

```html
<!DOCTYPE html>
<html lang="en">
<head>
<meta charset="utf-8">
<title>Ridgeline Clearing – Business Cards</title>
<link rel="stylesheet" href="https://fonts.googleapis.com/css2?family=Open+Sans:ital,wght@0,600;0,800;1,700&display=swap">
<style>
  :root {
    --backdrop: #b2b2b2;
    --paper: #ffffff;
    --forest: #38521e;
    --sky: #00aeef;
    --soil: #5e4733;
    --ink: #3a3a3a;
    --wordmark-dark: #111111;
    --emblem-green: #4a6b2c;
    --emblem-sky: #7fd3f5;
  }
  html, body {
    margin: 0;
    padding: 0;
    width: 1000px;
    height: 1200px;
    overflow: hidden;
    background: var(--backdrop);
    font-family: "Open Sans", sans-serif;
  }
  .sheet {
    position: relative;
    width: 1000px;
    height: 1200px;
  }
  .card {
    position: absolute;
    left: 51px;
    width: 898px;
    height: 538px;
    display: block;
  }
  .card--front { top: 44px; background: var(--paper); }
  .card--back  { top: 626px; background: var(--sky); }
  .wordmark {
    font-family: "Open Sans", sans-serif;
    font-weight: 800;
    font-size: 43px;
  }
  .wordmark--dark { fill: var(--wordmark-dark); }
  .wordmark--light { fill: var(--paper); }
  .contact-name { font-weight: 600; font-size: 33px; fill: var(--ink); }
  .contact-role { font-weight: 600; font-size: 28px; fill: var(--ink); }
  .contact-line { font-weight: 600; font-size: 22px; fill: var(--ink); }
  .tagline {
    font-weight: 700;
    font-style: italic;
    font-size: 27px;
    fill: var(--paper);
  }
</style>
</head>
<body>
<div class="sheet">

  <!-- Front of card -->
  <svg class="card card--front" viewBox="0 0 898 538" xmlns="http://www.w3.org/2000/svg">
    <circle class="emblem" cx="245" cy="150" r="112" fill="var(--emblem-green)" role="img"
            aria-label="Company emblem artwork"></circle>
    <text class="wordmark wordmark--dark" x="242" y="318" text-anchor="middle" textLength="383" lengthAdjust="spacingAndGlyphs">RIDGELINE</text>
    <text class="wordmark wordmark--dark" x="242" y="355" text-anchor="middle" textLength="282" lengthAdjust="spacingAndGlyphs">CLEARING</text>

    <text class="contact-name" x="482" y="313">Dale Whitcombe</text>
    <text class="contact-role" x="483" y="346">Owner</text>

    <g class="icon icon--phone" transform="translate(484,362)">
      <rect width="27" height="27" rx="2" fill="var(--forest)"/>
      <path d="M8 6 l3 -1 l2 5 l-2 1.5 q1.5 3.5 5 5 l1.5 -2 l5 2 l-1 3 q-1 1.5 -3 1 q-9 -3 -11.5 -11.5 q-0.5 -2 1 -3z" fill="var(--paper)"/>
    </g>
    <text class="contact-line" x="517" y="384">5550147832</text>

    <g class="icon icon--mail" transform="translate(484,404)">
      <rect width="27" height="27" rx="2" fill="var(--forest)"/>
      <rect x="5" y="8" width="17" height="12" fill="none" stroke="var(--paper)" stroke-width="1.6"/>
      <path d="M5 8 l8.5 7 l8.5 -7 M5 20 l6 -6 M22 20 l-6 -6" fill="none" stroke="var(--paper)" stroke-width="1.4"/>
    </g>
    <text class="contact-line" x="517" y="426">ridgelineclearing@fieldmail.com</text>

    <path class="ground-wave" d="M0 447 C 30 435, 60 427, 110 428 C 300 432, 520 478, 700 474 C 800 472, 860 460, 898 451 L 898 538 L 0 538 Z" fill="var(--forest)"/>
  </svg>

  <!-- Back of card -->
  <svg class="card card--back" viewBox="0 0 898 538" xmlns="http://www.w3.org/2000/svg">
    <circle class="emblem" cx="452" cy="160" r="112" fill="var(--emblem-sky)" stroke="var(--paper)" stroke-width="4" role="img"
            aria-label="Company emblem artwork"></circle>
    <text class="wordmark wordmark--light" x="443" y="324" text-anchor="middle" textLength="383" lengthAdjust="spacingAndGlyphs">RIDGELINE</text>
    <text class="wordmark wordmark--light" x="443" y="361" text-anchor="middle" textLength="282" lengthAdjust="spacingAndGlyphs">CLEARING</text>

    <path id="tagline-curve" d="M84 456 C 300 460, 600 430, 820 400" fill="none"/>
    <text class="tagline">
      <textPath href="#tagline-curve">Forestry Mulching / Brush Removal /Disaster Clean Up</textPath>
    </text>

    <path class="soil-wave" d="M0 450 C 80 465, 160 473, 250 471 C 420 468, 560 460, 700 445 C 800 433, 860 435, 898 445 L 898 538 L 0 538 Z" fill="var(--soil)"/>
  </svg>

</div>
</body>
</html>
```